Business Card Design Project

for a second hand vintage clothing store. shop name is The Velvet Cupboard

Cards to be double sided

The name on the card is Joanna Whitfield

Information to put on card:

The Velvet Cupboard
Joanna Whitfield (no job title)
42/871 Dunmore St, Glenwick, Sydney, NSW, 2009.
Mobile: 0412 905 261
Email: thevelvetcupboard@mailbox.com.au
Web: www.thevelvetcupboard.com.au

Target Market(s)

Women looking at vintage clothing

Industry/Entity Type

Clothing

```html
<!DOCTYPE html>
<html lang="en">
<head>
<meta charset="utf-8">
<title>The Velvet Cupboard – Joanna Whitfield</title>
<link rel="stylesheet" href="https://fonts.googleapis.com/css2?family=Felipa&display=swap">
<style>
  :root {
    --card-lime: #d6de6e;
    --ink: #1a1410;
    --plum: #612b3d;
    --frame-line: #d6de6e;
    --logo-cream: #f1dcc0;
    --ornament-light: #c9d062;
    --ornament-deep: #aab14c;
  }
  * { margin: 0; padding: 0; box-sizing: border-box; }
  html, body {
    width: 1200px;
    height: 676px;
    overflow: hidden;
    background: var(--card-lime);
  }
  .business-card {
    position: relative;
    width: 1200px;
    height: 676px;
    overflow: hidden;
    background: var(--card-lime);
    font-family: "Felipa", serif;
    color: var(--ink);
  }
  .monogram-ornament {
    position: absolute;
    left: 22px;
    top: 104px;
    width: 440px;
    height: 536px;
  }
  .monogram-ornament svg { display: block; }
  .shop-panel {
    position: absolute;
    left: 550px;
    top: 14px;
    width: 618px;
    height: 465px;
  }
  .shop-panel svg { display: block; }
  .shop-name {
    position: absolute;
    left: 48px;
    top: 42px;
    width: 464px;
    height: 345px;
    display: flex;
    align-items: center;
    justify-content: center;
    font-size: 48px;
    line-height: 1;
    color: var(--logo-cream);
    white-space: nowrap;
  }
  .holder-name {
    position: absolute;
    left: 464px;
    top: 494px;
    font-size: 84px;
    line-height: 1;
    letter-spacing: 1px;
    white-space: nowrap;
  }
  .contact-mobile {
    position: absolute;
    left: 470px;
    top: 592px;
    font-size: 48px;
    line-height: 1;
    white-space: nowrap;
  }
</style>
</head>
<body>
  <main class="business-card">
    <div class="monogram-ornament" role="img" aria-label="Ornate calligraphic initial monogram with looping ink flourishes">
      <svg width="440" height="536" viewBox="0 0 440 536" aria-hidden="true">
        <defs>
          <linearGradient id="ornament-tone" x1="0" y1="0" x2="1" y2="1">
            <stop offset="0" stop-color="var(--ornament-light)"/>
            <stop offset="1" stop-color="var(--ornament-deep)"/>
          </linearGradient>
        </defs>
        <ellipse cx="220" cy="268" rx="218" ry="266" fill="url(#ornament-tone)"/>
      </svg>
    </div>

    <div class="shop-panel">
      <svg width="618" height="465" viewBox="0 0 618 465" aria-hidden="true">
        <rect x="0" y="0" width="618" height="465" fill="var(--plum)"/>
        <line x1="0" y1="0" x2="48" y2="42" stroke="var(--frame-line)" stroke-width="8"/>
        <line x1="618" y1="0" x2="512" y2="42" stroke="var(--frame-line)" stroke-width="8"/>
        <line x1="0" y1="465" x2="48" y2="387" stroke="var(--frame-line)" stroke-width="8"/>
        <line x1="618" y1="465" x2="512" y2="387" stroke="var(--frame-line)" stroke-width="8"/>
        <rect x="48" y="42" width="464" height="345" fill="var(--plum)" stroke="var(--frame-line)" stroke-width="10"/>
      </svg>
      <div class="shop-name">The Velvet Cupboard</div>
    </div>

    <p class="holder-name">Joanna Whitfield</p>
    <p class="contact-mobile">Mobile: 0412 905 261</p>
  </main>
</body>
</html>
```